Seniors Massage Care Business Needs a New Website

Hello,
We require a website to be designed and coded. The design and coding must be high quality. Our website host has requested files be in static HTML format if possible.

The business is a mobile massage service for seniors (elderly people). The designer should emphasise that the business is a mobile service

The website will only have 4 pages.

1. Home- very simple layout and minimal information
2. Massage Services- this houses all of the information about the different services etc.
3. Contact Us-
4. ホーム (this is the Japanese symbol for 'home')- All of the information on the home page (section 1) will be translated into Japanese and uploaded to the brief for the designers to insert.

There is no requirement for an online booking, just contact information. The words 'Make a Booking' can be used and should lead customers to the 'Contact Us' page.

I have attached the business logo in multiple formats for designers to use.

I will upload more content and images to use for the website by the end of this week.

Thank you. I look forward to working with the successful candidate.

Target Market(s)

People aged 50+ years

Industry/Entity Type

Massage Therapy

Coding

Coded - Design and coding required

Number of Pages Required

4 page

Font styles to use
Sans Serif

Colors
74cabd
abd036
9ccb3b
f6faec
ffffff

Requirements
Must have
• Copyright free images and photos that we have taken. Both are important.
• Simple and inviting design.
Nice to have
• Colours of the logo incorporated.
Should not have
• This business is not a massage shop, so no images of massage shops or day salons required.
• Not too much imagery as the design needs to be simple.

```html
<!DOCTYPE html>
<html lang="en">
<head>
<meta charset="utf-8">
<title>Golden Hands Mobile Massage – Home</title>
<link href="https://fonts.googleapis.com/css2?family=Lora:wght@400;700&family=Open+Sans:wght@400&display=swap" rel="stylesheet">
<style>
  :root {
    --teal: #74cabd;
    --green: #abd036;
    --leaf: #9ccb3b;
    --logo-green: #8cc63f;
    --ink: #222222;
    --muted: #777777;
    --quote-bg: #eeeeee;
    --footer-bg: #f4f4f4;
    --white: #ffffff;
    --dark: #2b2b2b;
  }
  * { box-sizing: border-box; margin: 0; padding: 0; }
  html, body { width: 1081px; height: 1200px; overflow: hidden; background: var(--white); }
  body { position: relative; font-family: "Lora", Georgia, serif; color: var(--ink); }

  .site-header { position: absolute; left: 0; top: 0; width: 1081px; height: 149px; }
  .main-nav { position: absolute; left: 119px; top: 47px; display: flex; gap: 22px; font-size: 12px; }
  .main-nav a { color: var(--ink); text-decoration: none; }
  .main-nav a.is-active { color: var(--teal); }
  .brand { position: absolute; left: 340px; top: 36px; width: 400px; text-align: center; color: var(--logo-green); }
  .brand-mark { display: block; width: 46px; height: 46px; margin: 0 auto 8px; border-radius: 50%; background: var(--logo-green); }
  .brand-name { font-size: 20px; letter-spacing: 0.5px; white-space: nowrap; }
  .header-contact { position: absolute; right: 122px; top: 48px; display: flex; align-items: center; gap: 6px; font-size: 11px; color: var(--leaf); }
  .header-contact svg { display: block; }
  .header-contact .sep { color: #bbb; margin: 0 4px; }

  .hero { position: absolute; left: 0; top: 149px; width: 1081px; height: 403px;
    background: linear-gradient(90deg, #3a3f3c 0%, #6b6f62 35%, #8a8c80 50%, #7fa65a 70%, #5f8a3c 100%); }
  .hero-caption { position: absolute; left: 119px; top: 208px; color: var(--white); }
  .hero-caption .kicker { font-size: 17px; }
  .hero-caption .title { font-size: 26px; font-weight: 700; letter-spacing: 0.5px; margin-top: 2px; }
  .hero-arrow { position: absolute; top: 190px; width: 22px; height: 36px; background: rgba(0,0,0,0.25); display: flex; align-items: center; justify-content: center; }
  .hero-arrow.prev { left: 0; }
  .hero-arrow.next { right: 0; }

  .booking { position: absolute; left: 119px; top: 513px; width: 843px; height: 209px; background: var(--green); }
  .booking h2 { position: absolute; top: 18px; width: 100%; text-align: center; color: var(--white); font-size: 18px; font-weight: 700; letter-spacing: 0.3px; }
  .field { position: absolute; height: 36px; background: var(--white); color: var(--muted); font-size: 11px; padding: 0 14px; display: flex; align-items: center; justify-content: space-between; }
  .submit { position: absolute; left: 387px; top: 151px; width: 68px; height: 32px; background: var(--dark); color: var(--white); font-family: "Lora", Georgia, serif; font-size: 11px; border: 0; }

  .welcome { position: absolute; left: 119px; top: 746px; width: 598px; }
  .welcome h1 { font-size: 29px; font-weight: 400; color: var(--teal); line-height: 1.2; }
  .welcome .lead { margin-top: 12px; font-size: 12px; line-height: 17px; color: var(--ink); }
  .welcome .body { margin-top: 9px; font-family: "Open Sans", Arial, sans-serif; font-size: 10px; line-height: 17.3px; color: var(--muted); }

  .testimonial { position: absolute; left: 119px; top: 930px; width: 598px; height: 124px; background: var(--quote-bg); padding: 22px 30px; }
  .testimonial p { font-size: 14.5px; line-height: 23px; color: #888; }
  .testimonial .qmark { font-size: 44px; line-height: 0; color: #c8c8c8; font-weight: 700; vertical-align: -14px; margin-right: 6px; }
  .testimonial .qmark.close { margin: 0 0 0 8px; }
  .testimonial-fold { position: absolute; left: 689px; top: 1054px; }
  .testimonial-author { position: absolute; left: 560px; top: 1060px; width: 127px; text-align: right; font-size: 12px; color: var(--teal); }

  .side-photo { position: absolute; left: 745px; top: 752px; width: 216px; height: 324px;
    background: linear-gradient(180deg, #d9d4c8 0%, #c9c2b4 45%, #ebebeb 75%, #f7f7f7 100%); }

  .site-footer { position: absolute; left: 0; top: 1106px; width: 1081px; height: 94px; background: var(--footer-bg); font-family: "Open Sans", Arial, sans-serif; color: #444; font-size: 10px; }
  .footer-nav { position: absolute; left: 119px; top: 29px; display: flex; gap: 8px; }
  .footer-nav a { color: #444; text-decoration: none; }
  .copyright { position: absolute; left: 119px; top: 52px; word-spacing: 2px; }
  .social { position: absolute; left: 878px; top: 35px; display: flex; gap: 6px; }
  .social a { width: 24px; height: 24px; border-radius: 50%; display: block; }
  .social .s1 { background: #3b5998; }
  .social .s2 { background: #1da1f2; }
  .social .s3 { background: #0e76a8; }
</style>
</head>
<body>

<header class="site-header">
  <nav class="main-nav">
    <a href="#" class="is-active">Home</a>
    <a href="#">About</a>
    <a href="#">Services</a>
    <a href="#">Reviews</a>
    <a href="#">Contact</a>
  </nav>
  <div class="brand">
    <span class="brand-mark"></span>
    <div class="brand-name">Golden Hands Mobile Massage</div>
  </div>
  <div class="header-contact">
    <svg width="10" height="8" viewBox="0 0 10 8"><rect x="0.5" y="0.5" width="9" height="7" fill="none" stroke="#9ccb3b"/><path d="M0.5 0.5 L5 4.5 L9.5 0.5" fill="none" stroke="#9ccb3b"/></svg>
    <span>hello@goldenhandsmassage.com</span>
    <span class="sep">|</span>
    <svg width="6" height="10" viewBox="0 0 6 10"><rect x="0.5" y="0.5" width="5" height="9" rx="1" fill="none" stroke="#9ccb3b"/><rect x="2.5" y="7.5" width="1" height="1" fill="#9ccb3b"/></svg>
    <span>0400 318 527</span>
  </div>
</header>

<section class="hero" role="img" aria-label="Photo of a massage therapist treating a client on a massage table on a garden patio beside a lawn and tree">
  <div class="hero-caption">
    <div class="kicker">Nullam vulputate id nulla</div>
    <div class="title">MASSAGE CARE</div>
  </div>
  <span class="hero-arrow prev"><svg width="10" height="18" viewBox="0 0 10 18"><path d="M9 1 L1 9 L9 17" fill="none" stroke="#ddd" stroke-width="1.2"/></svg></span>
  <span class="hero-arrow next"><svg width="10" height="18" viewBox="0 0 10 18"><path d="M1 1 L9 9 L1 17" fill="none" stroke="#ddd" stroke-width="1.2"/></svg></span>
</section>

<section class="booking">
  <h2>MAKE A BOOKING</h2>
  <div class="field" style="left:11px;top:57px;width:198px;">Name</div>
  <div class="field" style="left:219px;top:57px;width:198px;">Email</div>
  <div class="field" style="left:427px;top:57px;width:198px;">Phone</div>
  <div class="field" style="left:635px;top:57px;width:198px;">Address
    <svg width="8" height="5" viewBox="0 0 8 5"><path d="M0.5 0.5 L4 4 L7.5 0.5" fill="none" stroke="#777"/></svg></div>
  <div class="field" style="left:11px;top:104px;width:198px;">Zipcode</div>
  <div class="field" style="left:219px;top:104px;width:198px;">Date and Time
    <svg width="11" height="11" viewBox="0 0 11 11"><rect x="0.5" y="1.5" width="10" height="9" fill="none" stroke="#888"/><path d="M0.5 4 H10.5 M3 0 V3 M8 0 V3 M3.5 4 V10.5 M7 4 V10.5 M0.5 7 H10.5" stroke="#888" fill="none"/></svg></div>
  <div class="field" style="left:427px;top:104px;width:406px;">Message</div>
  <button class="submit" type="button">SUBMIT</button>
</section>

<section class="welcome">
  <h1>Welcome to Golden Hands Mobile Massage</h1>
  <p class="lead">Sed feugiat fringilla mi, interdum euismod purus congue id. In pellentesque tincidunt lacinia. Lorem ipsum dolor sit amet, consectetur adipiscing elit. Vestibulum vel lorem eu.</p>
  <p class="body">Duis vitae porttitor eros. Nullam vel porta ipsum, non tempus nulla. Vestibulum posuere ipsum vel interdum malesuada. Nulla tristique sed nunc nec sagittis. Maecenas finibus ultrices magna quis lacinia. In hac habitasse platea dictumst. Sed pellentesque fermentum elit, ac egestas leo volutpat quis. Donec vitae ultricies sem. Donec vehicula sem sit amet dapibus tincidunt. Etiam tempus, diam sit amet fermentum pharetra, nunc magna tristique nisi, non laoreet urna neque ut odio.</p>
</section>

<blockquote class="testimonial">
  <p><span class="qmark">&ldquo;</span>Praesent lacus leto libero, iaculis at interdum in, suscipit ut felis. Quisque elementum diam mauris, vitae mollis libero semper vitae. Vestibulum tincidunt arcu aliquam velit rutrum tristique.<span class="qmark close">&rdquo;</span></p>
</blockquote>
<svg class="testimonial-fold" width="28" height="20" viewBox="0 0 28 20"><path d="M0 0 H28 V20 Z" fill="#eeeeee"/></svg>
<div class="testimonial-author">Amelia, City</div>

<div class="side-photo" role="img" aria-label="Photo of a smiling therapist giving a back massage to a client covered with a white towel"></div>

<footer class="site-footer">
  <nav class="footer-nav">
    <a href="#">Home</a><span>|</span>
    <a href="#">About</a><span>|</span>
    <a href="#">Services</a><span>|</span>
    <a href="#">Reviews</a><span>|</span>
    <a href="#">Contact</a>
  </nav>
  <div class="copyright">Copyright &copy; 2016 Company name. All rights reserved.</div>
  <div class="social">
    <a href="#" class="s1" aria-label="Social profile"></a>
    <a href="#" class="s2" aria-label="Social profile"></a>
    <a href="#" class="s3" aria-label="Social profile"></a>
  </div>
</footer>

</body>
</html>
```